Website re-design

We are a successful furnished apartment provider in Boston. We currently are working on re-designing our website www.ribtenlofts.com to make it more modern, designer look and user friendly. We hired a designer, but are not happy with the designs proposed and want to improve on them. The winning design will be paid regardless of whether we stay with our current designer or not. We want ideas and functional page links to see how it will work. Platform we have chosen is wordpress. Feel free to propose others easy for us to update and modify. We do not like Joomla on which website is currently running. We do not like flash nor long load times.
Please use photos on our website for design presentations. www.ribtenlofts.com

Target Market(s)

doctors, nurses, business men but mostly business women, some post-medical students

Industry/Entity Type

Apartment

Requirements
Must have
• Quick action button for reservation form and a notification and email forwarding system to us of reservation information by potential clients. Blog required with feedback by guests allowed, we can censor which are published. Slide shows of apartments.
Should not have
• No movies.

```html
<!DOCTYPE html>
<html lang="en">
<head>
<meta charset="utf-8">
<title>Ribten Lofts Furnished Apartments</title>
<link href="https://fonts.googleapis.com/css2?family=Cinzel:wght@400;700&family=PT+Sans:wght@400&display=swap" rel="stylesheet">
<style>
:root{
  --bg:#1e1713;
  --header:#0b0908;
  --gold:#e2c272;
  --gold-soft:#d8bd77;
  --field:#6b5c37;
  --panel:#2e2419;
  --muted:#8d7f6a;
}
*{margin:0;padding:0;box-sizing:border-box}
html,body{width:1198px;height:1200px;overflow:hidden;background:var(--bg)}
body{position:relative;font-family:"PT Sans",sans-serif;color:var(--gold-soft)}
.site-header{position:absolute;left:0;top:0;width:1198px;height:124px;background:var(--header)}
.brand{position:absolute;left:20px;top:38px;display:flex;align-items:center;gap:14px}
.brand-dot{width:72px;height:72px;border-radius:50%;background:var(--gold)}
.brand-name{font-family:"Cinzel",serif;color:var(--gold);font-size:35px;line-height:1;letter-spacing:1px}
.brand-name small{display:block;font-size:13px;letter-spacing:3px;margin-top:6px}
.call{position:absolute;right:34px;top:26px;font-family:"Cinzel",serif;color:var(--gold);font-size:16px}
.call b{font-weight:400;font-size:22px;margin-left:4px}
.nav{position:absolute;right:28px;top:78px;display:flex;gap:34px;list-style:none}
.nav li{font-family:"Cinzel",serif;color:var(--gold);font-size:17px}
.hero{position:absolute;left:14px;top:132px;width:1170px;height:509px;background:linear-gradient(160deg,#b8a36a 0%,#8c7a4c 35%,#5e4a2c 65%,#2c2140 100%)}
.hero-band{position:absolute;left:0;top:373px;width:100%;height:68px;background:rgba(200,200,205,.45);display:flex;align-items:center;padding-left:33px;gap:20px}
.hero-title{font-family:"Cinzel",serif;color:#fff;font-size:22px;margin-right:4px}
.hero-link{display:flex;align-items:center;gap:8px;font-family:"Cinzel",serif;color:#fff;font-size:14px}
.dots{position:absolute;right:24px;top:456px;display:flex;gap:5px}
.dots span{width:14px;height:14px;border-radius:50%;background:#d6d6d6}
.section-title{font-family:"Cinzel",serif;font-weight:400;color:var(--gold);font-size:17px;letter-spacing:.5px}
.intro{position:absolute;left:30px;top:688px;width:550px}
.intro p{font-size:12.5px;line-height:21px;margin-top:20px}
.gallery{position:absolute;left:674px;top:688px}
.thumbs{display:grid;grid-template-columns:repeat(4,91px);gap:8px 6px;margin-top:27px;margin-left:3px}
.thumb{width:91px;height:91px;border:1px solid var(--gold)}
.thumb.a{background:linear-gradient(135deg,#c9b9a6,#6b4a2c 60%,#4a3020)}
.thumb.b{background:linear-gradient(180deg,#d7c6ad,#8e7c68 55%,#3e4156)}
.reserve{position:absolute;left:13px;top:983px;width:1172px;height:173px;background:var(--panel);border:1px solid #3e3225}
.reserve .section-title{position:absolute;left:22px;top:18px;font-size:16px}
.reserve p{position:absolute;left:22px;top:52px;width:270px;font-size:12px;line-height:21px}
.field{position:absolute;left:336px;width:310px;height:29px;background:var(--field);color:#d9cba4;font-size:12px;padding:6px 12px}
.field.user{top:50px}.field.pass{top:86px}
.connect{position:absolute;left:768px;top:56px}
.connect .section-title{position:static;font-size:14px}
.social{display:flex;gap:10px;margin-top:12px}
.social span{width:16px;height:16px;border-radius:50%;background:#b28a3a}
.copyright{position:absolute;right:26px;top:1172px;font-size:10px;color:var(--muted)}
</style>
</head>
<body>
<header class="site-header">
  <div class="brand">
    <div class="brand-dot"></div>
    <div class="brand-name">Ribten Lofts<small>Furnished Apartments</small></div>
  </div>
  <div class="call">call us: <b>617 555 0142</b></div>
  <ul class="nav">
    <li>Home</li><li>Apartments</li><li>Reservations</li><li>Blog</li><li>Reviews</li><li>Boston</li><li>About Us</li>
  </ul>
</header>

<section class="hero" role="img" aria-label="Photo of a furnished studio with bed, armchairs and bay windows">
  <div class="hero-band">
    <span class="hero-title">Welcome to Ribten Lofts Furnished Apartments</span>
    <span class="hero-link"><svg width="34" height="28" viewBox="0 0 34 28"><rect x="1" y="9" width="32" height="18" fill="#eee"/><path d="M1 2l31 0 0 6-31 0z" fill="#eee"/><path d="M6 2l4 6M14 2l4 6M22 2l4 6" stroke="#888" stroke-width="2"/></svg>watch videos</span>
    <span class="hero-link"><svg width="32" height="26" viewBox="0 0 32 26"><rect x="1" y="5" width="30" height="20" rx="3" fill="#eee"/><rect x="10" y="1" width="12" height="5" fill="#eee"/><circle cx="16" cy="15" r="6" fill="#999"/></svg>watch photos</span>
    <span class="hero-link"><svg width="30" height="30" viewBox="0 0 30 30"><path d="M15 4a11 11 0 1 1-10 6" fill="none" stroke="#ddd" stroke-width="4"/><path d="M1 6l9 1-4 8z" fill="#ddd"/></svg>virual tour</span>
  </div>
  <div class="dots"><span></span><span></span><span></span><span></span></div>
</section>

<section class="intro">
  <h2 class="section-title">Ribten Lofts Furnished Apartments</h2>
  <p>Ribten Lofts is proud to offer some of the best furnished apartments in Boston. Our locations are in the trendiest area of the city: the South End. In the South End neighborhood, you will find wonderful restaurants, theaters, cafes and artist lofts. Our short term and extended stay apartments are very, very clean. We also offer the latest designer layouts: hardwood floors, Wireless Dsl, Cable TV, flat screen in most apartments, washer and dryer, cookware, cotton linens.</p>
  <p>Please click links on left for photo galleries, pricing, availability and reservation form and write us for more information.</p>
</section>

<section class="gallery">
  <h2 class="section-title">Ribten Lofts Furnished Apartments pictures</h2>
  <div class="thumbs">
    <div class="thumb a" role="img" aria-label="Living area photo"></div>
    <div class="thumb b" role="img" aria-label="Bedroom photo"></div>
    <div class="thumb a" role="img" aria-label="Living area photo"></div>
    <div class="thumb b" role="img" aria-label="Bedroom photo"></div>
    <div class="thumb a" role="img" aria-label="Living area photo"></div>
    <div class="thumb b" role="img" aria-label="Bedroom photo"></div>
    <div class="thumb a" role="img" aria-label="Living area photo"></div>
    <div class="thumb b" role="img" aria-label="Bedroom photo"></div>
  </div>
</section>

<section class="reserve">
  <h2 class="section-title">Reservation form:</h2>
  <p>Would you like to be informed of Ribten Lofts special offers? If so please opt in to our emails. You may also opt out at any time on this page:</p>
  <div class="field user">username</div>
  <div class="field pass">password</div>
  <div class="connect">
    <h3 class="section-title">Connect with us</h3>
    <div class="social"><span></span><span></span></div>
  </div>
</section>

<footer class="copyright">© Ribten Lofts 2010 - All Rights Reserved</footer>
</body>
</html>
```